Wine gifting platform needs redeem/decline page

Vintaro is a wine gifting platform. Users can send wine gifts to one or many people, the recipients will then receive an email with instructions on how to redeem their wine.

This is what we need: After clicking the link in the email they will be taken to the redeem/decline page/flow where they will choose their preferred wine and enter their shipping address. I have uploaded videos of both the decline and the redeem flows.

- All existing form fields, informational text, and error messages needs to be incorporated into the new design but otherwise you have creative freedom on presentation.
- We have four gift tiers: Silver, Gold, Platinum, and Diamond. We would like the redemption page to highlight this with different colors (or something else!) that's glanceable. I have attached screenshots to highlight these.
- Our target audience is professional and corporate but we want the redemption process to feel elegant and sleek. We want it to feel like a premium experience just like the wine they'll receive.

I would prefer Sketch files over Photoshop.

Target Market(s)

Professional, corporate

Number of Pages Required

3 page

Requirements
Must have
• All fields, all 3 steps of the wizard, information, and error messages/styles in the flow videos (attached)

```html
<!DOCTYPE html>
<html lang="en">
<head>
<meta charset="utf-8">
<title>Vintaro – Redeem Your Gift</title>
<link href="https://fonts.googleapis.com/css2?family=Nunito+Sans:wght@400;600;700&display=swap" rel="stylesheet">
<style>
:root{
  --brand:#1f47b3;
  --primary:#2f5ec4;
  --accent-light:#b9f0fb;
  --accent-pale:#dcf6fc;
  --accent-soft:#e3f8fd;
  --success:#6cc11a;
  --ink:#222;
  --muted:#666;
  --line:#e6e6e6;
  --field-line:#e2e2e2;
  --grey-btn:#8f8f8f;
  --wine:#5a1414;
}
*{box-sizing:border-box;margin:0;padding:0}
html,body{width:1200px;height:3620px;overflow:hidden;background:#fff}
body{font-family:"Nunito Sans",sans-serif;color:var(--ink);position:relative}
.screen{position:absolute;left:53px;width:1089px;background:#fff;box-shadow:0 2px 10px rgba(0,0,0,.12)}
.site-header{height:76px;display:flex;align-items:center;justify-content:center;box-shadow:0 3px 6px rgba(0,0,0,.05)}
.brand-name{font-size:46px;font-weight:700;color:var(--brand);letter-spacing:.5px}
.stepper{position:absolute;top:127px;left:0;width:100%;height:49px}
.step{position:absolute;top:0;height:49px;border:1px solid var(--line);border-radius:25px;display:flex;align-items:center;padding-left:6px;font-size:14px;color:#333;background:#fff}
.step-num{width:36px;height:36px;border-radius:50%;background:var(--primary);color:#fff;display:flex;align-items:center;justify-content:center;font-size:15px;margin-right:14px}
.step-num.done{background:var(--success)}
.step-link{position:absolute;top:24px;height:0;border-top:1px dashed #bbb}
.rule{position:absolute;left:101px;width:888px;border-top:1px solid var(--line)}
.center{text-align:center}
.collection{position:absolute;left:101px;top:261px;width:888px;height:188px;background:var(--accent-light);border-radius:10px;padding:34px 56px 0}
.collection h1{font-size:26px;font-weight:700;text-align:center;margin-bottom:20px}
.collection p{font-size:13.5px;line-height:25px;text-align:center;color:#333}
.section-title{position:absolute;left:0;width:100%;text-align:center;font-size:26px;font-weight:700}
.tabs{position:absolute;left:359px;top:597px;width:371px;height:61px;border:2px solid var(--line);border-radius:31px;display:flex;align-items:center;justify-content:space-between;padding:0 6px}
.tab{width:112px;height:49px;border-radius:25px;background:#f3f3f3;display:flex;align-items:center;justify-content:center;font-size:16px}
.tab.active{background:var(--accent-light)}
.wine-grid{position:absolute;left:101px;top:703px;display:grid;grid-template-columns:repeat(4,214px);grid-auto-rows:269px;gap:11px 11px}
.wine-card{border:1px solid #dff4f9;position:relative;text-align:center}
.wine-card.selected{background:var(--accent-pale);border-color:var(--accent-pale)}
.bottle{position:absolute;left:86px;top:34px;width:42px;height:118px;border-radius:12px 12px 8px 8px;background:linear-gradient(180deg,#3a0c0c,var(--wine) 60%,#2a0808)}
.wine-name{position:absolute;top:172px;width:100%;font-size:17px;font-weight:600}
.detail-btn{position:absolute;left:35px;top:206px;width:143px;height:34px;border-radius:17px;background:var(--accent-light);font-size:13.5px;font-weight:600;display:flex;align-items:center;justify-content:center}
.detail-btn.active{background:var(--primary);color:#fff}
.btn{position:absolute;height:48px;border-radius:5px;color:#fff;font-size:18px;font-weight:700;display:flex;align-items:center;justify-content:center;gap:10px}
.btn-primary{background:var(--primary)}
.btn-back{background:var(--grey-btn)}
.btn svg{width:18px;height:14px}
.form-card{position:absolute;left:101px;top:346px;width:888px;height:606px;background:#f8f8f8;border-radius:10px;box-shadow:0 3px 8px rgba(0,0,0,.08)}
.field{position:absolute;height:41px;width:383px;background:#fff;border:1px solid var(--field-line);border-radius:3px;font-size:14px;color:#777;display:flex;align-items:center;padding-left:25px}
.field.select{width:251px}
.field.select::after{content:"";position:absolute;right:25px;top:18px;border:5px solid transparent;border-top-color:#555}
.group-label{position:absolute;left:60px;top:162px;font-size:18px}
.check-row{position:absolute;left:53px;display:flex;align-items:center;font-size:14px;color:#555}
.box{width:24px;height:24px;border:1px solid #ccc;border-radius:4px;background:#fff;margin-right:18px}
.confirm-card{position:absolute;left:101px;top:265px;width:888px;height:543px;background:var(--accent-soft);border-radius:10px}
.confirm-lead{position:absolute;top:36px;width:100%;text-align:center;font-size:22px;line-height:32px;color:#333}
.info-card{position:absolute;left:123px;width:643px;background:#fff;border:1px solid var(--line)}
.address-lines{font-size:14px;line-height:23px;text-align:center;padding-top:12px;color:#333}
.product-name{position:absolute;left:32px;top:28px;font-size:18px}
.product-desc{position:absolute;left:32px;top:54px;width:470px;font-size:13.5px;line-height:25px;color:#555;text-align:justify}
.product-bottle{position:absolute;left:548px;top:16px;width:34px;height:118px;border-radius:10px 10px 6px 6px;background:linear-gradient(180deg,#3a0c0c,var(--wine) 60%,#2a0808)}
</style>
</head>
<body>

<!-- Step 1: choose gift -->
<section class="screen" style="top:87px;height:1408px">
  <header class="site-header"><span class="brand-name">Vintaro</span></header>
  <div class="stepper">
    <div class="step" style="left:199px;width:189px"><span class="step-num">1</span>Choose Your Gift</div>
    <span class="step-link" style="left:388px;width:84px"></span>
    <div class="step" style="left:472px;width:188px"><span class="step-num">2</span>Enter Your Adress</div>
    <span class="step-link" style="left:660px;width:81px"></span>
    <div class="step" style="left:741px;width:150px"><span class="step-num">3</span>Confirm</div>
  </div>
  <div class="rule" style="top:223px"></div>
  <div class="collection">
    <h1>Diamond Collection</h1>
    <p>Lorem ipsum dolor sit amet, consectetur adipiscing elit, sed do eiusmod tempor incididunt ut labore et dolore magna aliqua. Quis ipsum suspendisse ultrices gravida. Risus commodo viverra maecenas accumsan lacus vel facilisis.</p>
  </div>
  <div class="rule" style="top:487px"></div>
  <h2 class="section-title" style="top:530px">Choose your gift from the Diamond Collection</h2>
  <div class="tabs">
    <span class="tab active">Red</span><span class="tab">White</span><span class="tab">Rose</span>
  </div>
  <div class="wine-grid">
    <div class="wine-card selected"><div class="bottle" role="img" aria-label="Pinot Noir bottle"></div><div class="wine-name">Pinot Noir</div><div class="detail-btn active">View Details</div></div>
    <div class="wine-card"><div class="bottle" role="img" aria-label="Sangiovese bottle"></div><div class="wine-name">Sangiovese</div><div class="detail-btn">View Details</div></div>
    <div class="wine-card"><div class="bottle" role="img" aria-label="Cabernet Sauvignon bottle"></div><div class="wine-name">Cabernet Sauvignon</div><div class="detail-btn">View Details</div></div>
    <div class="wine-card"><div class="bottle" role="img" aria-label="Grenache bottle"></div><div class="wine-name">Grenache</div><div class="detail-btn">View Details</div></div>
    <div class="wine-card"><div class="bottle" role="img" aria-label="Pinot Noir bottle"></div><div class="wine-name">Pinot Noir</div><div class="detail-btn">View Details</div></div>
    <div class="wine-card"><div class="bottle" role="img" aria-label="Sangiovese bottle"></div><div class="wine-name">Sangiovese</div><div class="detail-btn">View Details</div></div>
    <div class="wine-card"><div class="bottle" role="img" aria-label="Cabernet Sauvignon bottle"></div><div class="wine-name">Cabernet Sauvignon</div><div class="detail-btn">View Details</div></div>
    <div class="wine-card"><div class="bottle" role="img" aria-label="Grenache bottle"></div><div class="wine-name">Grenache</div><div class="detail-btn">View Details</div></div>
  </div>
  <div class="btn btn-primary" style="left:486px;top:1296px;width:118px">Next
    <svg viewBox="0 0 18 14"><path d="M1 7h15M10 1l6 6-6 6" fill="none" stroke="#fff" stroke-width="1.6"/></svg></div>
</section>

<!-- Step 2: address -->
<section class="screen" style="top:1550px;height:1007px">
  <header class="site-header"><span class="brand-name">Vintaro</span></header>
  <div class="stepper">
    <div class="step" style="left:199px;width:189px"><span class="step-num done">1</span>Choose Your Gift</div>
    <span class="step-link" style="left:388px;width:84px"></span>
    <div class="step" style="left:472px;width:188px"><span class="step-num">2</span>Enter Your Adress</div>
    <span class="step-link" style="left:660px;width:81px"></span>
    <div class="step" style="left:741px;width:150px"><span class="step-num">3</span>Confirm</div>
  </div>
  <div class="rule" style="top:224px"></div>
  <h2 class="section-title" style="top:265px">Enter Your Address</h2>
  <form class="form-card">
    <div class="field" style="left:53px;top:41px">First Name</div>
    <div class="field" style="left:451px;top:41px">Last Name</div>
    <div class="field" style="left:53px;top:97px">Email Address</div>
    <div class="field" style="left:451px;top:97px">Phone</div>
    <div class="group-label">Address</div>
    <div class="field" style="left:53px;top:206px">Address</div>
    <div class="field" style="left:451px;top:206px">Address(Apt/Floor/Suite)</div>
    <div class="field select" style="left:53px;top:262px">City</div>
    <div class="field select" style="left:319px;top:262px">State</div>
    <div class="field select" style="left:585px;top:262px">Postal Code</div>
    <div style="position:absolute;left:53px;top:342px;width:782px;border-top:1px solid var(--line)"></div>
    <div class="check-row" style="top:368px"><span class="box"></span>I want to subscribe to emails from Vintaro to learn how to quickly and easily send wine gifts.</div>
    <div class="check-row" style="top:410px"><span class="box"></span>I confirm that I am of legal drinking age in my state.</div>
    <div class="check-row" style="top:453px"><span class="box"></span>I agree to the Privacy Policy and Terms of Services.</div>
    <div class="btn btn-back" style="left:319px;top:511px;width:118px"><svg viewBox="0 0 18 14"><path d="M17 7H2M8 1L2 7l6 6" fill="none" stroke="#fff" stroke-width="1.6"/></svg>Back</div>
    <div class="btn btn-primary" style="left:451px;top:511px;width:118px">Next<svg viewBox="0 0 18 14"><path d="M1 7h15M10 1l6 6-6 6" fill="none" stroke="#fff" stroke-width="1.6"/></svg></div>
  </form>
</section>

<!-- Step 3: confirm -->
<section class="screen" style="top:2618px;height:878px">
  <header class="site-header"><span class="brand-name">Vintaro</span></header>
  <div class="stepper">
    <div class="step" style="left:199px;width:189px"><span class="step-num done">1</span>Choose Your Gift</div>
    <span class="step-link" style="left:388px;width:84px"></span>
    <div class="step" style="left:472px;width:188px"><span class="step-num done">2</span>Enter Your Adress</div>
    <span class="step-link" style="left:660px;width:81px"></span>
    <div class="step" style="left:741px;width:150px"><span class="step-num">3</span>Confirm</div>
  </div>
  <div class="rule" style="top:224px"></div>
  <div class="confirm-card">
    <p class="confirm-lead">Your gift will be shipped in 1-3 business days and you will receive a tracking #<br>to your email.</p>
    <div class="info-card" style="top:127px;height:105px">
      <div class="address-lines">AA FF<br>48 Sample Ave, Hudson, NY 12534<br>+1 555-010-0199 - aa@vnt.co</div>
    </div>
    <div class="info-card" style="top:245px;height:150px">
      <div class="product-name">Pinot Noir</div>
      <p class="product-desc">Lorem ipsum dolor sit amet, consectetur adipiscing elit, sed do eiusmod tempor incididunt ut labore et dolore magna aliqua. Ut enim ad minim veniam, quis nostrud exercitation ullamco laboris nisi ut aliquip.</p>
      <div class="product-bottle" role="img" aria-label="Pinot Noir bottle"></div>
    </div>
    <div class="btn btn-back" style="left:319px;top:441px;width:118px"><svg viewBox="0 0 18 14"><path d="M17 7H2M8 1L2 7l6 6" fill="none" stroke="#fff" stroke-width="1.6"/></svg>Back</div>
    <div class="btn btn-primary" style="left:451px;top:441px;width:127px">Submit<svg viewBox="0 0 18 14"><path d="M1 7h15M10 1l6 6-6 6" fill="none" stroke="#fff" stroke-width="1.6"/></svg></div>
  </div>
</section>

</body>
</html>
```